College audience knows my web site is bad. HELP Escape Room needs makeover

New escape room in college town needs web site to impress.
Need you to make my sad attempt at WIX better
Black silver vivid yellow. I have logo as starting point. Prefer something I can update. I have site that I made as example but I need more professional work.
Possible future design work. Thanks.

Target Market(s)

Younger. Games

Industry/Entity Type

College

Number of Pages Required

3 page

Font styles to use
Sans Serif

Colors
000000
fbed22
eaeaea
cbcbcb

Requirements
Must have
• Logo I just purchsed through plume orchard. Black silver vivid yellow .
Nice to have
• Photo gallery where I can add photos
• Contact page

```html
<!DOCTYPE html>
<html lang="en">
<head>
<meta charset="utf-8">
<title>The Vaults of KTQ — Puzzle Simulation Game</title>
<link rel="stylesheet" href="https://fonts.googleapis.com/css2?family=Exo+2:wght@400;500&family=Open+Sans:wght@400;600&display=swap">
<style>
:root{
  --black:#000000;
  --ink:#1b1b1b;
  --yellow:#fbed22;
  --yellow-soft:#f4e62a;
  --light:#eaeaea;
  --silver:#cbcbcb;
  --panel:#f1f1f1;
  --text:#2a2a2a;
  --dark:#161616;
  --white:#ffffff;
}
*{box-sizing:border-box;margin:0;padding:0}
html,body{width:1200px;height:2908px;overflow:hidden}
body{font-family:"Open Sans",Arial,sans-serif;color:var(--text);background:var(--white);position:relative}
.heading{font-family:"Exo 2",Arial,sans-serif;font-weight:400;letter-spacing:1px;text-transform:uppercase;text-align:center}

/* Hero */
.hero{position:absolute;left:0;top:0;width:1200px;height:662px;overflow:hidden}
.hero-photo{position:absolute;inset:0;background:radial-gradient(ellipse at 55% 45%,#8c8b86 0%,#5f5e5a 45%,#2f2e2c 100%)}
.topbar{position:absolute;left:0;top:0;width:1200px;height:62px;background:rgba(0,0,0,.55)}
.brand{position:absolute;left:101px;top:0;width:190px;height:160px;background:var(--black);display:flex;align-items:center;justify-content:center;text-align:center;padding:0 14px}
.brand-name{font-family:"Exo 2",Arial,sans-serif;font-weight:500;font-size:22px;line-height:1.2;color:var(--yellow);text-transform:uppercase;letter-spacing:1px}
.nav{position:absolute;right:96px;top:24px;display:flex;gap:52px;list-style:none}
.nav a{font-family:"Open Sans",Arial,sans-serif;font-size:13px;color:var(--white);text-decoration:none;text-transform:uppercase}
.nav a.is-active{color:var(--yellow)}
.hero-title{position:absolute;left:0;top:355px;width:1200px;text-align:center;color:var(--white)}
.hero-title h1{font-family:"Exo 2",Arial,sans-serif;font-weight:400;font-size:58px;letter-spacing:2px;line-height:1}
.hero-title p{font-family:"Exo 2",Arial,sans-serif;font-size:32px;letter-spacing:1px;margin-top:8px}
.slide-arrow{position:absolute;top:342px;width:32px;height:32px;border-radius:50%;background:rgba(0,0,0,.45);display:flex;align-items:center;justify-content:center}
.slide-arrow.prev{left:56px}
.slide-arrow.next{left:1118px}

/* Features */
.features{position:absolute;left:0;top:662px;width:1200px;height:503px;background:linear-gradient(135deg,var(--yellow-soft),var(--yellow) 60%,#f7e826)}
.features .heading{position:absolute;left:0;top:72px;width:1200px;font-size:34px;color:var(--ink)}
.feature{position:absolute;top:186px;width:300px;text-align:center}
.feature:nth-of-type(1){left:95px}
.feature:nth-of-type(2){left:446px}
.feature:nth-of-type(3){left:797px}
.feature-icon{width:106px;height:106px;border:2px solid var(--ink);border-radius:50%;margin:0 auto;display:flex;align-items:center;justify-content:center}
.feature-icon span{width:44px;height:44px;border-radius:50%;background:var(--ink);display:flex;align-items:center;justify-content:center}
.feature h3{font-family:"Exo 2",Arial,sans-serif;font-weight:400;font-size:20px;letter-spacing:1px;margin-top:18px;color:var(--ink)}
.feature p{font-size:12px;line-height:21px;margin-top:8px;color:var(--ink)}

/* Gallery */
.gallery{position:absolute;left:0;top:1165px;width:1200px;height:663px;background:var(--panel)}
.gallery .heading{position:absolute;left:0;top:64px;width:1200px;font-size:32px;color:var(--ink)}
.rule{position:absolute;left:537px;width:126px;height:2px;background:var(--silver)}
.rule::after{content:"";position:absolute;left:43px;top:0;width:40px;height:2px;background:var(--yellow)}
.gallery .rule{top:121px}
.gallery-grid{position:absolute;left:99px;top:155px;width:1002px;height:430px;display:grid;grid-template-columns:repeat(4,1fr);grid-template-rows:repeat(2,1fr)}
.tile:nth-child(1){background:linear-gradient(135deg,#7d7a74,#3d3c39)}
.tile:nth-child(2){background:linear-gradient(135deg,#c8ccd6,#2e4a8a)}
.tile:nth-child(3){background:linear-gradient(135deg,#6e5a52,#c9b8aa)}
.tile:nth-child(4){background:linear-gradient(180deg,#9a9690,#3a3937)}
.tile:nth-child(5){background:linear-gradient(135deg,#5e5e5e,#a8a8a6)}
.tile:nth-child(6){background:linear-gradient(135deg,#2e2b28,#6a5d4a)}
.tile:nth-child(7){background:linear-gradient(135deg,#4a4a48,#9bb8c9)}
.tile:nth-child(8){background:linear-gradient(180deg,#3b5566,#1b2a33)}

/* Welcome */
.welcome{position:absolute;left:0;top:1828px;width:1200px;height:377px;background:linear-gradient(135deg,var(--yellow),var(--yellow-soft))}
.welcome .heading{position:absolute;left:0;top:88px;width:1200px;font-size:32px;color:var(--ink)}
.welcome .rule{top:143px}
.welcome-copy{position:absolute;left:160px;top:176px;width:880px;text-align:center;font-size:11.5px;line-height:20px;color:var(--ink)}
.welcome-copy p+p{margin-top:16px}

/* Contact */
.contact{position:absolute;left:0;top:2205px;width:1200px;height:555px;background:linear-gradient(180deg,#1e1e1e,var(--dark))}
.contact .heading{position:absolute;left:0;top:62px;width:1200px;font-size:32px;color:var(--white)}
.contact-info{position:absolute;top:140px;display:flex;align-items:center;gap:14px;color:var(--white);font-size:13px;line-height:20px}
.contact-info.address{left:214px}
.contact-info.phone{left:505px}
.contact-info.email{left:760px}
.info-icon{width:34px;height:34px;border:1.5px solid var(--white);border-radius:50%;display:flex;align-items:center;justify-content:center;flex:none}
.contact-form{position:absolute;left:214px;top:210px;width:771px;height:300px}
.field{position:absolute;left:0;width:339px;height:38px;background:var(--white);border:none;font-family:"Open Sans",Arial,sans-serif;font-size:11px;color:#555;padding:0 14px;display:flex;align-items:center}
.field.message{left:360px;top:0;width:411px;height:197px;align-items:flex-start;padding-top:12px}
.submit{position:absolute;left:267px;top:237px;width:239px;height:45px;background:var(--yellow);border:none;border-radius:3px;font-family:"Open Sans",Arial,sans-serif;font-weight:600;font-size:18px;color:var(--ink)}

/* Footer */
.footer{position:absolute;left:0;top:2760px;width:1200px;height:148px;background:var(--white);text-align:center}
.social{display:flex;justify-content:center;gap:9px;padding-top:20px}
.social span{width:28px;height:28px;border-radius:50%;background:#3a3a3a}
.footer-nav{display:flex;justify-content:center;gap:10px;list-style:none;margin-top:14px;font-size:11px;color:#333;text-transform:uppercase}
.footer-nav li+li::before{content:"/";margin-right:10px;font-style:italic}
.copyright{font-size:11px;color:#333;margin-top:8px}
</style>
</head>
<body>

<header class="hero">
  <div class="hero-photo" role="img" aria-label="Photo of a man in a blue shirt scratching his head in a long grey concrete corridor"></div>
  <div class="topbar"></div>
  <div class="brand"><span class="brand-name">The Vaults<br>of KTQ</span></div>
  <ul class="nav">
    <li><a class="is-active" href="#">Home</a></li>
    <li><a href="#">About Us</a></li>
    <li><a href="#">Rooms</a></li>
    <li><a href="#">FAQ</a></li>
    <li><a href="#">Blog</a></li>
    <li><a href="#">Contact Us</a></li>
  </ul>
  <div class="hero-title">
    <h1>THE VAULTS OF KTQ</h1>
    <p>Puzzle Simulation Game</p>
  </div>
  <div class="slide-arrow prev"><svg width="12" height="12" viewBox="0 0 12 12"><path d="M8 1 3 6l5 5" fill="none" stroke="#fff" stroke-width="2"/></svg></div>
  <div class="slide-arrow next"><svg width="12" height="12" viewBox="0 0 12 12"><path d="M4 1l5 5-5 5" fill="none" stroke="#fff" stroke-width="2"/></svg></div>
</header>

<section class="features">
  <h2 class="heading">Game in Reality</h2>
  <div class="feature">
    <div class="feature-icon"><span><svg width="24" height="24" viewBox="0 0 24 24"><path d="M12 3a6 6 0 0 0-3.5 10.9V17h7v-3.1A6 6 0 0 0 12 3z" fill="none" stroke="#fbed22" stroke-width="1.8"/><path d="M9.5 20h5" stroke="#fbed22" stroke-width="1.8"/></svg></span></div>
    <h3>TASK</h3>
    <p>Solve every clue in the room, work as a team and find the hidden way out before the end.</p>
  </div>
  <div class="feature">
    <div class="feature-icon"><span><svg width="24" height="24" viewBox="0 0 24 24"><circle cx="12" cy="12" r="8" fill="none" stroke="#fbed22" stroke-width="1.8"/><path d="M12 7v5h4" fill="none" stroke="#fbed22" stroke-width="1.8"/></svg></span></div>
    <h3>TIME</h3>
    <p>Sixty minutes on the clock. Every second counts as you race to crack the final lock and walk free.</p>
  </div>
  <div class="feature">
    <div class="feature-icon"><span><svg width="24" height="24" viewBox="0 0 24 24"><path d="M5 9h4a2.5 2.5 0 1 1 5 0h4v4a2.5 2.5 0 1 0 0 5v2H5z" fill="#fbed22"/></svg></span></div>
    <h3>IMPRESSION</h3>
    <p>Real rooms, real props and real tension. A game night your friends will talk about long after you escape.</p>
  </div>
</section>

<section class="gallery">
  <h2 class="heading">Photo Gallery</h2>
  <div class="rule"></div>
  <div class="gallery-grid">
    <div class="tile" role="img" aria-label="Photo of a figure leaping through a bare concrete cell"></div>
    <div class="tile" role="img" aria-label="Photo of a businessman standing at the edge of a blue maze"></div>
    <div class="tile" role="img" aria-label="Photo of a man with an umbrella in a narrow corridor"></div>
    <div class="tile" role="img" aria-label="Photo of a man walking on a checkered floor"></div>
    <div class="tile" role="img" aria-label="Photo of a man facing a dim brick room"></div>
    <div class="tile" role="img" aria-label="Photo of a lantern before a dark stone wall"></div>
    <div class="tile" role="img" aria-label="Photo of a woman stepping toward a keyhole shaped opening to a green field"></div>
    <div class="tile" role="img" aria-label="Photo of small figures inside a misty blue labyrinth"></div>
  </div>
</section>

<section class="welcome">
  <h2 class="heading">Welcome to the Vaults of KTQ</h2>
  <div class="rule"></div>
  <div class="welcome-copy">
    <p>The Vaults of KTQ is a live puzzle game built for curious minds. You and your crew are locked inside a themed room full of riddles, codes and hidden objects. Work together, think fast and follow every clue to unlock the door before time runs out. Bring classmates, friends or coworkers and test how well you solve problems under pressure.</p>
    <p>Each room has its own story, from a forgotten office to a maze of endless halls. Games suit groups of two to eight players and no experience is needed. Our game masters watch over every session and can offer hints when you get stuck. Book a slot online, gather your team and see if you have what it takes to escape.</p>
  </div>
</section>

<section class="contact">
  <h2 class="heading">Contact Us</h2>
  <div class="contact-info address">
    <span class="info-icon"><svg width="14" height="16" viewBox="0 0 14 16"><path d="M7 1a5 5 0 0 0-5 5c0 4 5 9 5 9s5-5 5-9a5 5 0 0 0-5-5z" fill="#fff"/><circle cx="7" cy="6" r="1.8" fill="#1e1e1e"/></svg></span>
    <span>48 Lantern Row, Suite B-4<br>Millbrook, OR 97001</span>
  </div>
  <div class="contact-info phone">
    <span class="info-icon"><svg width="14" height="14" viewBox="0 0 14 14"><path d="M3 1l2.5 2.5-1.3 2a7 7 0 0 0 4.3 4.3l2-1.3L13 11l-1.5 2C6 13 1 8 1 2.5z" fill="#fff"/></svg></span>
    <span>Call Us :<br>(+1) 555.014.2290</span>
  </div>
  <div class="contact-info email">
    <span class="info-icon"><svg width="15" height="12" viewBox="0 0 15 12"><rect x="1" y="1" width="13" height="10" fill="none" stroke="#fff" stroke-width="1.4"/><path d="M1 1l6.5 5L14 1" fill="none" stroke="#fff" stroke-width="1.4"/></svg></span>
    <span>E - Mail :<br>info@thevaultsofktq.com</span>
  </div>
  <form class="contact-form">
    <div class="field" style="top:0">Name :</div>
    <div class="field" style="top:52px">Email :</div>
    <div class="field" style="top:104px">Phone :</div>
    <div class="field" style="top:156px">Subject :</div>
    <div class="field message">Message :</div>
    <button class="submit" type="button">Submit Now</button>
  </form>
</section>

<footer class="footer">
  <div class="social"><span></span><span></span><span></span><span></span><span></span></div>
  <ul class="footer-nav">
    <li>Home</li><li>About Us</li><li>Rooms</li><li>FAQ</li><li>Blog</li><li>Contact Us</li>
  </ul>
  <p class="copyright">2016 © Copyrights The Vaults Of KTQ.All Rights Reserved</p>
</footer>

</body>
</html>
```